Mobile phone signal boosting solutions needs a website

We need a website design for the reselling of a mobile signal boosting product set. These solutions are Vexlor exempt and will provide an indoor signal for mobile phones. We would like to see designs that incorporate the colours and feel of our logo. The domain will be
openmeadow.com / co.uk
Overview of the company and how it is to be used: Open meadow (domain name) will work with business and end user to provide mobile signal boosting – where people struggle indoors with a mobile signal our solutions will help by finding the smallest signal and boosting it, allowing users to use voice and data over their mobile network (please note this is not wireless signal boosting)
Number of Pages:
-Home
-Solutions / How it works
-Case Studies
-Contact
Text content: Currently just use placeholders
Technical specs : Wordpress and ability to use CMS if that’s relevant
Target Market(s)
Business professional all markets /high end residential
Coded - Design and coding required
4 page

```html
<!DOCTYPE html>
<html lang="en">
<head>
<meta charset="utf-8">
<title>Open Meadow – Mobile Signal Boosting</title>
<link rel="stylesheet" href="https://fonts.googleapis.com/css2?family=Roboto+Condensed:wght@400;500;700&display=swap">
<style>
  :root {
    --bg-deep: #0b0c0a;
    --bg-olive: #18200f;
    --bg-amber: #1e1608;
    --text-main: #ffffff;
    --text-muted: #b9b9b4;
    --accent: #e8a423;
    --button-bg: #ffffff;
    --button-text: #111111;
  }
  * { margin: 0; padding: 0; box-sizing: border-box; }
  html, body {
    width: 1200px;
    height: 594px;
    overflow: hidden;
    background: var(--bg-deep);
    font-family: "Roboto Condensed", "Arial Narrow", sans-serif;
    color: var(--text-main);
  }
  .page {
    position: relative;
    width: 1200px;
    height: 594px;
    overflow: hidden;
  }
  .hero-backdrop {
    position: absolute;
    inset: 0;
    background:
      radial-gradient(ellipse 60% 55% at 75% 20%, var(--bg-olive) 0%, transparent 70%),
      radial-gradient(ellipse 55% 50% at 20% 85%, var(--bg-amber) 0%, transparent 70%),
      var(--bg-deep);
  }
  .site-header {
    position: absolute;
    top: 0;
    left: 0;
    right: 0;
    height: 130px;
    display: flex;
    align-items: center;
  }
  .brand {
    position: absolute;
    left: 70px;
    top: 52px;
    display: flex;
    align-items: center;
    gap: 8px;
    font-weight: 500;
    font-size: 20px;
    color: var(--text-main);
    text-decoration: none;
    letter-spacing: -0.2px;
  }
  .brand-mark {
    width: 14px;
    height: 14px;
    background: var(--accent);
  }
  .main-nav {
    position: absolute;
    left: 219px;
    top: 58px;
    display: flex;
    gap: 0;
  }
  .main-nav a {
    font-size: 12px;
    font-weight: 500;
    color: var(--text-main);
    text-decoration: none;
    margin-right: 25px;
  }
  .hero-copy {
    position: absolute;
    left: 39px;
    top: 170px;
    width: 320px;
  }
  .hero-title {
    font-size: 49px;
    font-weight: 500;
    line-height: 1;
    letter-spacing: -0.3px;
  }
  .hero-question {
    margin-top: 22px;
    font-size: 54px;
    font-weight: 500;
    line-height: 1;
    color: transparent;
    -webkit-text-stroke: 1.6px var(--text-main);
  }
  .hero-lede {
    margin-top: 22px;
    width: 200px;
    font-size: 12px;
    line-height: 25px;
    font-weight: 500;
    color: var(--text-muted);
  }
  .hero-cta {
    display: flex;
    align-items: center;
    justify-content: center;
    margin-top: 32px;
    width: 266px;
    height: 42px;
    border-radius: 21px;
    background: var(--button-bg);
    color: var(--button-text);
    font-size: 15px;
    font-weight: 700;
    text-decoration: none;
    letter-spacing: 0.3px;
  }
</style>
</head>
<body>
<div class="page">
  <div class="hero-backdrop" role="img" aria-label="Dark, softly lit background scene in deep olive and amber tones"></div>

  <header class="site-header">
    <a class="brand" href="#">
      <span class="brand-mark"></span>
      <span class="brand-name">Open Meadow</span>
    </a>
    <nav class="main-nav">
      <a href="#">How It Works</a>
      <a href="#">Case Studies</a>
      <a href="#">Contact</a>
    </nav>
  </header>

  <section class="hero-copy">
    <h1 class="hero-title">Open Meadow</h1>
    <p class="hero-question">Do you?</p>
    <p class="hero-lede">If not, DON'T WORRY we've got you covered!</p>
    <a class="hero-cta" href="#">BOOST IT!</a>
  </section>
</div>
</body>
</html>
```